Shipping Container Sales & Leasing Flyer

We need a flyer that is going to be presented and left behind while prospecting potential customers. The service we are selling is the sale, rental and customization of 20' and 40' shipping containers.

We provide new and used containers to customers for various reasons, mainly storage. We also custom modify containers into storage units, mobile offices, mobile job site storage, command centers, pump houses, garages, living space, the only limit is the customers imagination.

I would like our company logo and phone / email at the bottom but the design should showcase some of the attached images ive provided as examples and have spots where we can list the types of equipment we have for sale and the various types of conversions we can offer.

Please also tie in to the colour scheme of our logo.

Target Market(s)

Moving & Storage, Construction, Contractors, Business to Business, Any business that needs portable storage, Landscapers, Property Maintenance companies.

Industry/Entity Type

Shipping

Font styles to use
Serif
Sans Serif

Requirements
Must have
• Professional feel, clean original design.
Nice to have
• Tie in to our logo colour scheme.
Should not have
• Bulky or crowded look

```html
<!DOCTYPE html>
<html lang="en">
<head>
<meta charset="utf-8">
<title>Corran Management – Shipping Container Flyer</title>
<link href="https://fonts.googleapis.com/css2?family=Oswald:wght@500;600&family=Lato:ital,wght@0,700;1,400;1,700&family=Roboto:wght@500;700;900&family=Roboto+Condensed:wght@400&display=swap" rel="stylesheet">
<style>
  :root{
    --green:#5aa323;
    --green-dark:#2f7a12;
    --green-light:#8cd13c;
    --ink:#1d1d1d;
    --charcoal:#2b2b2d;
    --paper:#ffffff;
    --mist:#ececec;
  }
  html,body{margin:0;padding:0;overflow:hidden;background:#ffffff;}
  .flyer{position:relative;width:902px;height:1200px;overflow:hidden;background:var(--mist);font-family:"Lato",sans-serif;}
  .hero-photo{position:absolute;left:0;top:0;width:610px;height:440px;
    background:linear-gradient(90deg,#8d9396 0%,#a9afb2 55%,rgba(236,236,236,0) 100%);}
  .shapes{position:absolute;left:0;top:0;}
  .brand{position:absolute;left:597px;top:90px;width:240px;text-align:center;}
  .brand-mark{width:58px;height:58px;border-radius:50%;background:var(--green);margin:0 auto 14px;}
  .brand-name{font-family:"Roboto",sans-serif;font-weight:900;font-size:46px;letter-spacing:6px;color:var(--green);line-height:1;}
  .brand-sub{font-family:"Roboto",sans-serif;font-weight:500;font-size:12px;letter-spacing:5px;color:var(--ink);margin-top:6px;}
  .headline{position:absolute;left:0;width:902px;text-align:center;white-space:nowrap;line-height:1;}
  .headline-top{top:486px;font-family:"Roboto",sans-serif;font-weight:700;font-size:43px;color:var(--green);}
  .headline-main{top:546px;font-family:"Oswald",sans-serif;font-weight:600;font-size:59px;color:var(--ink);transform:scaleY(1.12);}
  .provide{position:absolute;left:0;width:902px;top:662px;text-align:center;font-family:"Roboto",sans-serif;white-space:nowrap;}
  .provide-title{font-weight:700;font-size:31px;line-height:36px;color:var(--ink);}
  .provide-text{font-weight:500;font-size:22px;line-height:25px;letter-spacing:.6px;color:#fff;margin-top:4px;}
  .modify-pill{position:absolute;left:0;top:826px;width:512px;height:46px;background:#111;border-radius:0 24px 24px 0;
    color:#fff;font-family:"Roboto Condensed",sans-serif;font-size:28px;line-height:46px;padding-left:38px;box-sizing:border-box;white-space:nowrap;}
  .conversions{position:absolute;left:40px;top:905px;width:446px;margin:0;padding:0;list-style:none;
    columns:2;column-gap:0;font-style:italic;font-size:16.5px;color:var(--ink);}
  .conversions li{line-height:25px;padding-left:16px;position:relative;white-space:nowrap;}
  .conversions li::before{content:"";position:absolute;left:2px;top:9px;width:8px;height:8px;border-radius:50%;background:var(--green);}
  .tagline{position:absolute;left:34px;top:1020px;font-style:italic;font-weight:700;font-size:28px;line-height:34px;color:var(--green-dark);white-space:nowrap;}
  .booking{position:absolute;left:0;top:1073px;width:565px;height:127px;
    background:linear-gradient(90deg,#2f7a12 0%,#62ad26 55%,#2f7a12 100%);border-top:4px solid var(--green-light);box-sizing:border-box;}
  .booking-label{position:absolute;left:56px;top:31px;font-family:"Roboto",sans-serif;font-weight:500;font-size:30px;line-height:36px;color:#fff;}
  .booking-icon{position:absolute;left:260px;top:27px;}
  .booking-number{position:absolute;left:320px;top:22px;font-family:"Oswald",sans-serif;font-weight:600;font-size:44px;line-height:54px;color:#fff;}
  .gallery-photo{position:absolute;left:585px;width:275px;border:5px solid #fff;box-sizing:border-box;}
  .gallery-photo.units{top:803px;height:170px;background:linear-gradient(180deg,#cfd7dd 0%,#b8bcbf 60%,#5b5e62 100%);}
  .gallery-photo.interior{top:988px;height:172px;background:linear-gradient(90deg,#c9ccd0 0%,#e6e8ea 60%,#6fa9cf 100%);}
</style>
</head>
<body>
<div class="flyer">
  <div class="hero-photo" role="img" aria-label="Photo of a grey 20 foot shipping container in a yard"></div>

  <svg class="shapes" width="902" height="1200" viewBox="0 0 902 1200" aria-hidden="true">
    <path d="M0 440 C250 480 650 460 902 250 L902 1200 L0 1200 Z" fill="var(--charcoal)"/>
    <path d="M0 392 C260 445 640 430 902 200 L902 262 C660 470 260 480 0 432 Z" fill="var(--green)"/>
    <path d="M0 432 C260 480 660 470 902 262 L902 272 C660 482 260 492 0 442 Z" fill="var(--green-light)"/>
    <path d="M0 458 C300 420 650 430 902 485 L902 790 L565 790 L565 1200 L0 1200 Z" fill="var(--paper)"/>
    <path d="M0 700 C300 630 650 630 902 668 L902 752 C650 790 300 795 0 786 Z" fill="var(--green-dark)"/>
    <path d="M0 786 C300 795 650 790 902 752 L902 762 C650 800 300 806 0 796 Z" fill="var(--green-light)"/>
    <rect x="565" y="790" width="337" height="410" fill="var(--charcoal)"/>
  </svg>

  <div class="brand">
    <div class="brand-mark"></div>
    <div class="brand-name">CORRAN</div>
    <div class="brand-sub">MANAGEMENT</div>
  </div>

  <div class="headline headline-top">SALE, RENTAL AND CUSTOMIZATION OF</div>
  <div class="headline headline-main">20' AND 40' SHIPPING CONTAINERS</div>

  <div class="provide">
    <div class="provide-title">WE PROVIDE</div>
    <div class="provide-text">NEW AND USED CONTAINERS TO CUSTOMERS FOR<br>VARIOUS REASONS, MAINLY STORAGE</div>
  </div>

  <div class="modify-pill">We also custom modify containers into</div>
  <ul class="conversions">
    <li>Storage units</li>
    <li>Mobile offices</li>
    <li>Mobile job site storage</li>
    <li>Command centers,</li>
    <li>Pump houses</li>
    <li>Garages</li>
    <li>Living space</li>
  </ul>
  <div class="tagline">The only limit is the customers imagination</div>

  <div class="booking">
    <div class="booking-label">For Booking</div>
    <svg class="booking-icon" width="44" height="44" viewBox="0 0 44 44" aria-hidden="true">
      <circle cx="22" cy="22" r="19" fill="none" stroke="#111" stroke-width="3"/>
      <path d="M15 12 l5 0 l2 6 l-3 2 c1.5 3 3.5 5 6 6 l2 -3 l6 2 l0 5 c-10 1 -19 -8 -18 -18 Z" fill="#111"/>
    </svg>
    <div class="booking-number">0123456789</div>
  </div>

  <div class="gallery-photo units" role="img" aria-label="Photo of a container converted into storage units with roll-up doors"></div>
  <div class="gallery-photo interior" role="img" aria-label="Photo of a container interior fitted with shelving and a workbench"></div>
</div>
</body>
</html>
```